Sehr zuverlässige, motivierte Arbeitsweise. Danke!
Zielgruppe
Ich bin eine Fotokünstlerin und Autorin. Meine Zielgruppe sind interkulturell interessierte (meist Frauen) mit einem Interesse an Ästethik, Exotik und persönlichen Geschichten. Das Buchcover soll neugierig machen auf das Buch. Ich würde es gerne im Taschenbuch und E-Book Format haben.
Aufgabenstellung
Ich habe eine Idee für ein Buchcover:
Leere Flugzeugabflughalle in großem internationalen Flughafen (Panama oder karibisch wirkend)
Farben eher Pastelltöne Grau/Rosé/Lila. (Es wäre schön, wenn es klar wird, dass es ein Buch ist, dass in den 90ern in Panama spielt)
Mädchen (ungefähr 8/9 Jahre alt; mit Teddybär in der Hand, der hinter sich her gezogen wird) mit Mutter, Vater und Bruder (ungefähr 11/12 Jahre alt) (Familie) in schwarz Silhouette mit Koffern
Draußen: Palmen zu sehen in sattem grün.
Ich bin auch offen für ganz andere Ideen. Der Regenwald funktioniert leider thematisch nicht wirklich für mein Buch ist mir aufgefallen, nachdem ich teilweise sehr schöne Vorschläge dafür bekommen habe. Danke.
Ich habe auch ungefähre Vorstellungen bezüglich der Fonts:
Die Font Besipiele sollen ähnlich sein im Endergebnis wie auf den mitgeschickten Bildern zu sehen.
Das Buch heißt: Lantern Pages - Tage hinter dem Meer.
Autorin: Marit Solveig Brenner
Formate: Taschenbuch und E-Book
Lantern Pages sollte ähnlich wie im “Font 1” sein und Tage hinter dem Meer im “Font 2” sein.
Mein Name auf der Vorderseite sollte schlicht und schnörkellos weit unten auf der Seite stehen.
Das Logo sollte in klein irgendwo auf der Rückseite des Buches zu sehen sein.
“Veradalairport” ist der Flughafen in Panama. Mein ehemaliges vorläufiges Buchcover.
“Zomerlicht” ist ein Originalfoto vom Veradal Airport, dass verwendet werden könnte.
Inhalt des Buches kurz gefasst (sollte auf der Rückseite des Buches zu sehen sein):
Aus einer Zeit vor Internet, Videoanruf und Kurznachricht.
Briefe einer Mutter an ihren Freunde, Familie und Bekannte in Halvern, Deutschland in Panama City, Panama aufgeschrieben und abgeschickt.
Kommentare einer Tochter hierzu und Erinnerungen an diese Zeit in Retrospektive aufgeschrieben, als Erwachsene fast gleichen Alters mit der Mutt..

```html
<!DOCTYPE html>
<html lang="de">
<head>
<meta charset="utf-8">
<title>Lantern Pages – Tage hinter dem Meer</title>
<link href="https://fonts.googleapis.com/css2?family=Merriweather:wght@900&family=Montserrat:wght@500;600&family=Gochi+Hand&display=swap" rel="stylesheet">
<style>
  :root {
    --page-bg: #f2f2f2;
    --back-deep: #3f4a43;
    --back-mid: #6f7f77;
    --back-mist: #a7b5b2;
    --front-green: #2f8a3c;
    --front-leaf: #57b04a;
    --front-yellow: #f4cf2a;
    --front-orange: #f3a25a;
    --front-pink: #e2205e;
    --front-navy: #1f2d5a;
    --text-light: #ffffff;
    --logo-pink: #f2b8c6;
  }
  * { margin: 0; padding: 0; box-sizing: border-box; }
  html, body { width: 1200px; height: 800px; overflow: hidden; }
  body {
    background: var(--page-bg);
    font-family: "Montserrat", sans-serif;
    position: relative;
  }
  .cover {
    position: absolute;
    top: 130px;
    width: 360px;
    height: 540px;
    overflow: hidden;
    box-shadow: 0 12px 30px rgba(0,0,0,.18);
  }
  .cover--back { left: 220px; }
  .cover--front { left: 620px; }

  .artwork { position: absolute; inset: 0; }
  .artwork--back {
    background:
      radial-gradient(ellipse at 70% 15%, var(--back-mist) 0%, transparent 55%),
      linear-gradient(170deg, var(--back-mid) 0%, #5d6e64 45%, var(--back-deep) 100%);
  }
  .artwork--front {
    background:
      radial-gradient(ellipse at 55% 35%, var(--front-yellow) 0%, var(--front-orange) 28%, transparent 55%),
      linear-gradient(180deg, transparent 62%, var(--front-pink) 82%, var(--front-navy) 100%),
      linear-gradient(90deg, var(--front-green) 0%, var(--front-leaf) 30%, transparent 45%, transparent 60%, var(--front-leaf) 78%, var(--front-green) 100%),
      var(--front-yellow);
  }

  .blurb {
    position: absolute;
    left: 36px;
    right: 36px;
    top: 112px;
    color: var(--text-light);
    font-size: 11.5px;
    font-weight: 500;
    line-height: 1.45;
  }
  .blurb p { margin-bottom: 14px; }

  .imprint {
    position: absolute;
    right: 30px;
    bottom: 40px;
    display: flex;
    align-items: center;
    gap: 6px;
    color: var(--text-light);
    font-size: 10px;
    font-weight: 500;
  }
  .imprint__dot {
    width: 34px; height: 34px;
    border-radius: 50%;
    background: var(--logo-pink);
  }

  .author {
    position: absolute;
    right: 22px;
    top: 404px;
    color: var(--text-light);
    font-weight: 600;
    font-size: 15px;
    letter-spacing: .3px;
  }
  .title {
    position: absolute;
    left: 18px;
    top: 420px;
    color: var(--text-light);
    font-family: "Merriweather", serif;
    font-weight: 900;
    font-size: 41px;
    white-space: nowrap;
    text-shadow: 0 1px 3px rgba(0,0,0,.25);
  }
  .subtitle {
    position: absolute;
    left: 40px;
    top: 476px;
    color: var(--text-light);
    font-family: "Gochi Hand", cursive;
    font-size: 31px;
    white-space: nowrap;
  }
</style>
</head>
<body>
  <section class="cover cover--back">
    <div class="artwork artwork--back" role="img" aria-label="Gedämpftes Dschungelgemälde in Grau- und Grüntönen"></div>
    <div class="blurb">
      <p>Aus einer Zeit vor Internet, Videoanruf und Kurznachricht.</p>
      <p>Briefe einer Mutter an Freunde, Familie und Bekannte in Halvern, geschrieben und abgeschickt aus einer Stadt weit hinter dem Meer.</p>
      <p>Kommentare einer Tochter dazu und Erinnerungen an diese Zeit, rückblickend aufgeschrieben, als Erwachsene fast im gleichen Alter wie die Mutter damals.</p>
      <p>Ein Einblick in die 90er Jahre, fern der Heimat. Kulturschock inklusive.</p>
      <p>Ein Buch. Zwei Lebenswelten. Zwei unterschiedliche Geschichten. Ein ehrlicher Rückblick in die 90er Jahre. Eine persönliche Geschichte.</p>
    </div>
    <div class="imprint"><span class="imprint__dot"></span>Brenner Edition</div>
  </section>

  <section class="cover cover--front">
    <div class="artwork artwork--front" role="img" aria-label="Farbenfrohes Dschungelgemälde mit großen Blättern, gelbem Licht und einem pinkfarbenen Weg, auf dem ein Mädchen mit Rucksack geht"></div>
    <p class="author">Marit Solveig Brenner</p>
    <h1 class="title">Lantern Pages</h1>
    <p class="subtitle">Tage hinter dem Meer</p>
  </section>
</body>
</html>
```